Fahrzeugbeschriftung für Sanitär- und Heizungshandwerker
Zielgruppe
Heizung Sanitär Wärmepumpe Badezimmer aus einer Hand und Energieberatung
Aufgabenstellung
Einfach modern und ansprechbar

```html
<!DOCTYPE html>
<html lang="de">
<head>
<meta charset="utf-8">
<title>NORVALT – Fahrzeugbeschriftung</title>
<link rel="stylesheet" href="https://fonts.googleapis.com/css2?family=Audiowide&family=Open+Sans:ital,wght@0,400;1,400&display=swap">
<style>
  :root {
    --bg-top: #2f2f31;
    --bg-bottom: #57575a;
    --band: #6d6e71;
    --panel: #ffffff;
    --ink: #1d1d27;
    --orange: #e0951f;
    --blue: #1560b0;
    --red: #d41f26;
    --white: #ffffff;
  }
  html, body {
    margin: 0;
    padding: 0;
    width: 1034px;
    height: 1200px;
    overflow: hidden;
  }
  body {
    background: linear-gradient(180deg, var(--bg-top), var(--bg-bottom) 90%);
  }
  .wrap-sheet { display: block; width: 1034px; height: 1200px; }
  .brand-name { font-family: "Audiowide", sans-serif; }
  .tagline { font-family: "Open Sans", sans-serif; font-style: italic; }
  .service { font-family: "Audiowide", sans-serif; font-style: italic; fill: var(--ink); }
  .contact-phone { font-family: "Audiowide", sans-serif; }
  .contact-mail { font-family: "Open Sans", sans-serif; }
</style>
</head>
<body>
<svg class="wrap-sheet" viewBox="0 0 1034 1200" xmlns="http://www.w3.org/2000/svg">
  <defs>
    <clipPath id="side-clip"><rect x="60" y="110" width="915" height="270" rx="22"/></clipPath>
    <clipPath id="rear-clip"><rect x="600" y="620" width="320" height="310" rx="22"/></clipPath>
  </defs>

  <!-- Side panel -->
  <g class="side-panel">
    <rect x="60" y="110" width="915" height="270" rx="22" fill="var(--panel)"/>
    <g class="side-colour-block" clip-path="url(#side-clip)">
      <rect x="790" y="230" width="185" height="8" fill="var(--orange)"/>
      <rect x="790" y="238" width="185" height="8" fill="var(--red)"/>
      <rect x="790" y="246" width="185" height="134" fill="var(--blue)"/>
    </g>
    <rect x="505" y="176" width="22" height="22" fill="var(--blue)"/>
    <text class="brand-name" x="538" y="200" font-size="32" fill="var(--ink)">NORVALT</text>
    <text class="tagline" x="584" y="220" font-size="13" fill="var(--ink)">HAUS- UND GEBÄUDETECHNIK</text>

    <text class="service" x="505" y="296" font-size="13">Heizung</text>
    <text class="service" x="505" y="314" font-size="13">Sanitär</text>
    <text class="service" x="505" y="332" font-size="13">Regenerative Energien</text>
    <text class="service" x="505" y="350" font-size="13">Sowie Energieberatung</text>

    <path class="phone-icon" d="M806 301 l3 -1 l2 3 l-1.5 1.5 q1 2 3 3 l1.5 -1.5 l3 2 l-1 3 q-6 0 -10 -10 z" fill="var(--white)"/>
    <text class="contact-phone" x="824" y="311" font-size="13" fill="var(--white)">0511 4620 918</text>
    <text class="contact-mail" x="806" y="329" font-size="11.5" fill="var(--white)">info@norvalt-technik.de</text>
  </g>

  <!-- Front panel -->
  <g class="front-panel">
    <rect x="110" y="640" width="330" height="250" rx="22" fill="var(--panel)"/>
    <rect x="198" y="778" width="17" height="17" fill="var(--blue)"/>
    <text class="brand-name" x="222" y="796" font-size="22" fill="var(--ink)">NORVALT</text>
    <text class="tagline" x="234" y="809" font-size="7.5" fill="var(--ink)">HAUS- UND GEBÄUDETECHNIK</text>
  </g>

  <!-- Rear panel -->
  <g class="rear-panel">
    <rect x="600" y="620" width="320" height="310" rx="22" fill="var(--panel)"/>
    <g class="rear-colour-block" clip-path="url(#rear-clip)">
      <rect x="600" y="872" width="320" height="6" fill="var(--orange)"/>
      <rect x="600" y="878" width="320" height="6" fill="var(--red)"/>
      <rect x="600" y="884" width="320" height="46" fill="var(--blue)"/>
    </g>
    <rect x="662" y="654" width="204" height="37" fill="var(--ink)"/>
    <rect x="670" y="660" width="14" height="14" fill="var(--blue)"/>
    <text class="brand-name" x="692" y="676" font-size="21" fill="var(--white)">NORVALT</text>
    <text class="tagline" x="718" y="688" font-size="8.5" fill="var(--white)">HAUS- UND GEBÄUDETECHNIK</text>

    <g fill="var(--ink)">
      <polygon points="664,710 668,710 666,716 662,716"/>
      <polygon points="664,726 668,726 666,732 662,732"/>
      <polygon points="664,741 668,741 666,747 662,747"/>
      <polygon points="664,757 668,757 666,763 662,763"/>
    </g>
    <text class="service" x="678" y="717" font-size="12">Heizung</text>
    <text class="service" x="678" y="733" font-size="12">Sanitär</text>
    <text class="service" x="678" y="748" font-size="12">Regenerative Energien</text>
    <text class="service" x="678" y="764" font-size="12">Sowie Energieberatung</text>

    <text class="tagline" x="889" y="815" font-size="12" fill="var(--ink)" text-anchor="end">www.norvalt-technik.de</text>
    <path class="phone-icon" d="M780 832 l2.5 -1 l1.7 2.5 l-1.2 1.2 q0.8 1.7 2.5 2.5 l1.2 -1.2 l2.5 1.7 l-1 2.5 q-5 0 -8.2 -8.2 z" fill="var(--ink)"/>
    <text class="contact-phone" x="889" y="841" font-size="11" fill="var(--ink)" text-anchor="end">0511 4620 918</text>
    <text class="contact-mail" x="889" y="856" font-size="10" fill="var(--ink)" text-anchor="end">info@norvalt-technik.de</text>
  </g>

  <!-- Footer band -->
  <g class="footer-band">
    <rect x="0" y="1115" width="1034" height="85" fill="var(--band)"/>
    <rect x="788" y="1142" width="22" height="22" fill="var(--white)"/>
    <text class="brand-name" x="822" y="1166" font-size="30" fill="var(--white)">NORVALT</text>
    <text class="tagline" x="838" y="1182" font-size="10.5" fill="var(--white)">HAUS- UND GEBÄUDETECHNIK</text>
  </g>
</svg>
</body>
</html>
```